The Lantern Over The Hills

This is a book about the growth of a father and how that can help us relate to our Heavenly Father. It's a Christian growth and/or self-help book, talking about experiences any father might go through, the ups and downs, the triumphs and struggles of life. Something we can all relate to.

I would prefer some artwork like the attached - showing a father with 2 or 3 kids, no faces. Something colorful and catchy.

The subhead would be:

When Little Ones Show Us How To Trust,
Rest & Walk Beside The Shepherd

By Doug Pettersen

```html
<!DOCTYPE html>
<html lang="en">
<head>
<meta charset="utf-8">
<title>The Lantern Over The Hills — Book Cover</title>
<link rel="stylesheet" href="https://fonts.googleapis.com/css2?family=Cinzel:wght@400;700&family=Mulish:wght@400&display=swap">
<style>
  :root {
    --stage: #b9bbbd;
    --sky-top: #7fe9f7;
    --sky-mid: #bfe9e6;
    --glow: #fff8d8;
    --sun-gold: #f6d64a;
    --sun-orange: #f3a64a;
    --hill-blue: #8fb4c4;
    --title-red: #d90d10;
    --ink: #0a0a0a;
    --figure-dark: #141414;
    --white: #ffffff;
  }
  * { box-sizing: border-box; margin: 0; padding: 0; }
  html, body {
    width: 1200px; height: 972px; overflow: hidden;
    background: var(--stage);
  }
  .stage {
    width: 1200px; height: 972px;
    display: flex; align-items: center; justify-content: center;
  }
  .cover {
    position: relative;
    width: 564px; height: 910px;
    overflow: hidden;
    background: var(--sky-top);
  }
  .cover-sky {
    position: absolute; inset: 0;
    background:
      radial-gradient(ellipse 55% 32% at 58% 60%, var(--white) 0%, var(--glow) 28%, rgba(246,214,74,0.85) 55%, rgba(243,166,74,0) 100%),
      linear-gradient(180deg, var(--sky-top) 0%, var(--sky-mid) 28%, #f4e9a0 45%, var(--sun-gold) 58%, var(--sun-orange) 72%, var(--hill-blue) 84%, #3b3f44 92%);
  }
  .family-figures {
    position: absolute;
    left: 152px; top: 437px;
    width: 265px; height: 370px;
    border-radius: 60px 60px 0 0;
    background: linear-gradient(180deg, rgba(20,20,20,0.55) 0%, var(--figure-dark) 35%, var(--ink) 100%);
  }
  .ground-band {
    position: absolute; left: 0; right: 0; bottom: 0;
    height: 150px;
  }
  .title {
    position: absolute; left: 0; right: 0; top: 40px;
    text-align: center;
    font-family: "Cinzel", serif;
    font-weight: 700;
    color: var(--title-red);
    text-shadow: 0 2px 2px rgba(120,0,0,0.35);
    line-height: 1;
  }
  .title-small { display: block; font-size: 30px; letter-spacing: 1px; }
  .title-large { display: block; font-size: 74px; margin-top: 6px; }
  .title-link {
    display: flex; align-items: center; justify-content: center;
    gap: 10px; margin: 10px 0 8px;
    font-size: 28px;
  }
  .title-link::before, .title-link::after {
    content: ""; width: 132px; height: 2px;
    background: linear-gradient(90deg, rgba(217,13,16,0.2), var(--title-red));
  }
  .title-link::after { background: linear-gradient(90deg, var(--title-red), rgba(255,255,255,0.7)); }
  .title-hills { display: block; font-size: 100px; }
  .subtitle {
    position: absolute; left: 0; right: 0; top: 350px;
    text-align: center;
    font-family: "Mulish", sans-serif;
    font-size: 21px; line-height: 1.4;
    color: var(--ink);
  }
  .author {
    position: absolute; left: 0; right: 0; bottom: 36px;
    text-align: center;
    font-family: "Cinzel", serif;
    font-weight: 400;
    font-size: 38px; letter-spacing: 4px;
    color: var(--white);
  }
</style>
</head>
<body>
  <main class="stage">
    <section class="cover">
      <div class="cover-sky" role="img" aria-label="Bright sunburst over misty mountains and a lake"></div>
      <div class="family-figures" role="img" aria-label="Silhouette of a father carrying a small child on his shoulder and holding hands with two children, seen from behind"></div>
      <svg class="ground-band" viewBox="0 0 564 150" preserveAspectRatio="none" aria-hidden="true">
        <path d="M0 28 C 140 8, 330 12, 564 0 L 564 150 L 0 150 Z" fill="var(--ink)"/>
      </svg>
      <h1 class="title">
        <span class="title-small">THE</span>
        <span class="title-large">LANTERN</span>
        <span class="title-link">OVER THE</span>
        <span class="title-hills">HILLS</span>
      </h1>
      <p class="subtitle">When Little Ones Show Us How To Trust,<br>Rest &amp; Walk Beside The Shepherd</p>
      <p class="author">Doug Pettersen</p>
    </section>
  </main>
</body>
</html>
```